Buch-/eBook-Cover für Darmtherapie für Frauen
Von Herzen Danke. Das design ist super geworden. Ich glaube ich war nicht so einfach mit meinen Änderungen. Schnelle Kommunikation. DAAANKE!!!! Ich bin so glücklich
Zielgruppe
Darmtherapie für Frauen,
Mamas und Frauen mit Kinderwunsch
Babys und Kinder
Entdecke die transformierende
Kraft der Darmtherapie!
Wie eine Darmtherapie dein Immunsystem ganzheitlich regulieren und dir bei hormonellem Ungleichgewicht helfen kann, ohne deinen Körper durch einen vermeidbaren Ärztemarathon zusätzlich zu belasten.
Ich begleite dich auf deinem Weg in ein erfülltes (Mama) – Leben.
Weil ganzheitliche Gesundheit im Darm beginnt.
Ich möchte nicht, dass dieses Buch ein weiteres ist, das du liest und dann wieder vergisst. Dieses Buch soll dich durch deine verschiedenen Lebensphasen begleiten. Du kannst dir die Informationen und Werkzeuge herausnehmen, die zu deiner Situation und deiner Familie passen.
In diesem Buch findest du freie Felder, leere Seiten und Aufgaben, in denen du deine Gedanken und Notizen festhalten kannst. Hier findest du auch Zitate, Rezepte, Übungen und Anleitungen, die speziell auf deine Lebensphase und die deiner Kinder zugeschnitten sind.
Aufgabenstellung
Eyecather Titel. Eyecather Cover. Eilt nicht Cover mit einem Heilstein oder so. Evtl Titel des Flyers mit einarbeiten: Erlebe die wohltuende Wirkung der Darmbalance ( nur Vorschlag)
Es soll nicht der Flyer als Cover werden. Flyer dient nur der Firmen Farben etc
Richtiger eye Catcher Titel. Gern etwas provokativ

```html
<!DOCTYPE html>
<html lang="de">
<head>
<meta charset="utf-8">
<title>Entspannter leben mit Darmbalance – Buchcover</title>
<link rel="stylesheet" href="https://fonts.googleapis.com/css2?family=Bebas+Neue&family=Josefin+Sans:wght@600;700&family=Comic+Neue:wght@700&family=Montserrat:wght@400&display=swap">
<style>
  :root {
    --page-bg: #efefef;
    --cover-teal: #80bcc2;
    --navy: #34496e;
    --white: #ffffff;
    --title-shadow: #5b6a70;
    --ink: #111111;
    --slate: #6f7a84;
    --olive: #b5bb3a;
    --gut-pink: #ef9c93;
    --gut-blue: #7fb8dd;
  }
  * { margin: 0; padding: 0; box-sizing: border-box; }
  html, body { width: 1200px; height: 1034px; overflow: hidden; background: var(--page-bg); }
  .cover {
    position: absolute; left: 285px; top: 43px; width: 631px; height: 948px;
    background: var(--cover-teal); overflow: hidden;
  }
  .author {
    position: absolute; top: 36px; left: 0; width: 100%; text-align: center;
    font-family: "Josefin Sans", sans-serif; font-weight: 600; font-size: 29px;
    letter-spacing: 2.5px; color: var(--navy);
  }
  .brand {
    position: absolute; top: 17px; left: 508px; width: 108px; text-align: center;
  }
  .brand-dot { display: block; width: 96px; height: 96px; border-radius: 50%; background: var(--olive); margin: 0 auto 3px; }
  .brand-name { font-family: "Montserrat", sans-serif; font-size: 11px; color: var(--navy); white-space: nowrap; }
  h1 { font-weight: normal; }
  .title { position: absolute; left: 0; width: 100%; text-align: center; line-height: 1; display: block; }
  .title-line1 {
    top: 128px; font-family: "Bebas Neue", sans-serif; font-size: 98px; color: var(--white);
    letter-spacing: 5px; text-shadow: 4px 4px 0 var(--title-shadow);
  }
  .title-line2 {
    top: 227px; font-family: "Bebas Neue", sans-serif; font-size: 138px; color: var(--white);
    letter-spacing: 6px; text-shadow: 5px 5px 0 var(--title-shadow);
  }
  .title-mit {
    top: 364px; font-family: "Josefin Sans", sans-serif; font-weight: 700; font-size: 36px;
    color: var(--navy); letter-spacing: 3px;
  }
  .title-line3 {
    top: 405px; font-family: "Bebas Neue", sans-serif; font-size: 96px; color: var(--navy);
    letter-spacing: 6px;
  }
  .tagline {
    position: absolute; left: 56px; top: 515px;
    font-family: "Comic Neue", cursive; font-weight: 700; font-size: 27px; line-height: 43px;
    color: var(--ink); text-transform: uppercase; letter-spacing: 0.5px;
  }
  .gut-illustration {
    position: absolute; left: 335px; top: 498px; width: 271px; height: 449px;
    border-radius: 40% 40% 30% 30%;
    background: radial-gradient(ellipse at 50% 50%, var(--gut-pink) 0 50%, var(--gut-blue) 75%, transparent 77%);
  }
  .audience {
    position: absolute; left: 0; top: 805px; width: 324px; height: 114px;
    background: var(--slate); padding: 15px 0 0 40px;
    font-family: "Montserrat", sans-serif; font-size: 19px; line-height: 30px; color: var(--white);
  }
</style>
</head>
<body>
  <main class="cover">
    <div class="author">CARLA WENDT</div>
    <div class="brand"><span class="brand-dot"></span><span class="brand-name">Praxis Wendt</span></div>
    <h1>
      <span class="title title-line1">ENTSPANNTER</span>
      <span class="title title-line2">LEBEN</span>
      <span class="title title-mit">MIT</span>
      <span class="title title-line3">DARMBALANCE</span>
    </h1>
    <p class="tagline">Erlebe die<br>wohltuende<br>Wirkung der<br>Darmbalance</p>
    <div class="gut-illustration" role="img" aria-label="Illustration von Magen und Darm in Rosa und Hellblau"></div>
    <div class="audience">Darmtherapie für Frauen<br>Bei Kinderwunsch<br>Für Babys und Kinder</div>
  </main>
</body>
</html>
```